Creative & Professional Business Card for hair salon

We are looking to update our business cards. Our salon is creative, modern, progressive and professional and looking for a design that will reflect this.

```html
<!DOCTYPE html>
<html lang="en">
<head>
<meta charset="utf-8">
<title>Lumen Hair Studio – Business Cards</title>
<link rel="stylesheet" href="https://fonts.googleapis.com/css2?family=Great+Vibes&family=Roboto:wght@400;500&display=swap">
<style>
  :root{
    --page:#e9e9e7;
    --card-black:#121214;
    --damask-dark:#1d1d21;
    --sky:#8db7c6;
    --sky-deep:#7eaabb;
    --brand-light:#cfe3ec;
    --white:#ffffff;
    --ink:#0b0b0b;
  }
  *{box-sizing:border-box;margin:0;padding:0}
  html,body{width:1200px;height:873px;overflow:hidden}
  body{background:var(--page);font-family:"Roboto",Arial,sans-serif;position:relative}

  .card{position:absolute;top:278px;width:520px;height:316px;overflow:hidden;
    box-shadow:0 6px 18px rgba(0,0,0,.18)}
  .card--back{left:60px;background:var(--sky)}
  .card--front{left:620px;background:var(--card-black)}

  .texture{position:absolute;inset:0}
  .card--back .texture{background:linear-gradient(135deg,var(--sky) 0%,var(--sky-deep) 100%)}
  .card--front .texture{background:radial-gradient(circle at 60% 50%,var(--damask-dark) 0%,var(--card-black) 75%)}

  /* appointment side */
  .appointment{position:absolute;left:34px;top:30px;color:var(--white)}
  .appointment__title{font-size:17px;letter-spacing:.5px}
  .appointment__title em{display:block;font-family:"Great Vibes",cursive;font-style:normal;font-size:20px;margin-left:28px;margin-top:-2px}
  .field{display:flex;align-items:center;margin-top:10px}
  .field__label{width:52px;font-size:16px}
  .field__box{width:150px;height:26px;background:var(--white);opacity:.92}

  .divider{position:absolute;left:268px;top:40px;width:1px;height:186px;background:var(--white)}
  .contact{position:absolute;left:286px;top:150px;color:var(--white)}
  .contact__row{display:flex;align-items:center;gap:8px}
  .contact__phone{font-size:25px;font-weight:500;letter-spacing:.5px}
  .contact__web{font-size:14px;margin-top:6px}
  .icon{width:16px;height:16px;flex:none}

  .address-band{position:absolute;left:0;right:0;bottom:0;height:56px;background:var(--ink);
    display:flex;align-items:center;gap:12px;padding-left:26px;color:var(--white);font-size:21px}
  .address-band .pin{width:20px;height:26px;flex:none}

  /* brand side */
  .brand{position:absolute;left:0;right:0;top:118px;display:flex;justify-content:center;align-items:center;gap:14px;
    font-family:"Roboto",Arial,sans-serif;font-weight:400;font-size:34px;color:var(--brand-light);letter-spacing:.5px}
  .brand__mark{width:14px;height:14px;background:var(--brand-light);flex:none}
  .maker{position:absolute;left:0;right:0;top:176px;text-align:center;
    font-family:"Roboto",Arial,sans-serif;font-weight:400;font-size:17px;color:var(--brand-light);letter-spacing:2px}
</style>
</head>
<body>

<section class="card card--back" aria-label="Business card, appointment side">
  <div class="texture" role="img" aria-label="Soft blue damask pattern"></div>

  <div class="appointment">
    <p class="appointment__title">Your Next <em>Appointment</em></p>
    <div class="field"><span class="field__label">Date:</span><span class="field__box"></span></div>
    <div class="field"><span class="field__label">Time:</span><span class="field__box"></span></div>
  </div>

  <div class="divider"></div>

  <div class="contact">
    <div class="contact__row">
      <svg class="icon" viewBox="0 0 16 16" aria-hidden="true"><circle cx="8" cy="8" r="7" fill="none" stroke="#fff" stroke-width="1.3"/><path d="M5.5 4.5l1.5 1.5-1 1c.6 1.3 1.5 2.2 2.8 2.8l1-1 1.5 1.5-1.2 1.2C7.6 11 5 8.4 4.3 5.7z" fill="#fff"/></svg>
      <span class="contact__phone">61•7•5000•1234</span>
    </div>
    <div class="contact__row">
      <svg class="icon" viewBox="0 0 16 16" aria-hidden="true"><circle cx="8" cy="8" r="7" fill="none" stroke="#fff" stroke-width="1.3"/><ellipse cx="8" cy="8" rx="3" ry="7" fill="none" stroke="#fff" stroke-width="1"/><path d="M1 8h14" stroke="#fff" stroke-width="1"/></svg>
      <span class="contact__web">www.lumenhair.com.au</span>
    </div>
  </div>

  <div class="address-band">
    <svg class="pin" viewBox="0 0 20 26" aria-hidden="true"><path d="M10 0C4.5 0 0 4.4 0 9.8 0 17 10 26 10 26s10-9 10-16.2C20 4.4 15.5 0 10 0z" fill="#fff"/><circle cx="10" cy="9.5" r="3.6" fill="#0b0b0b"/></svg>
    <span>3/12 Harbour Lane Maroona Qld 4000</span>
  </div>
</section>

<section class="card card--front" aria-label="Business card, brand side">
  <div class="texture" role="img" aria-label="Dark damask pattern"></div>
  <p class="brand"><span class="brand__mark"></span>Lumen Hair Studio</p>
  <p class="maker">Jo Marlow</p>
</section>

</body>
</html>
```